Visitenkarten-Design für Autowerkstatt/-verwertung
Zielgruppe
Unser Unternehmen besteht aus zwei Bereiche:
- Autoverwertung
- Autowerkstatt
Aufgabenstellung
Informationen auf der Visitenkarte:
'Brunnhofer' - Logo
Lindenauer Str. 31
80993 München
Autoverwertung Autoteile
www.autoverwertung-brunnhofer-beispiel.de
info@autoverwertung-brunnhofer-beispiel.de
Autowerkstatt
www.auto-brunnhofer-beispiel.de
info@auto-brunnhofer-beispiel.de
Öffnungszeiten:
Mo-Fr
08.00 - 12.00 Uhr und 13.00 - 17.00 Uhr
Farblich sollte die Visitenkarte sich an das Logo anpassen. Visitenkarte 2-4 seitig.

```html
<!DOCTYPE html>
<html lang="de">
<head>
<meta charset="utf-8">
<title>Brunnhofer Visitenkarte</title>
<link href="https://fonts.googleapis.com/css2?family=Open+Sans:wght@400;700;800&display=swap" rel="stylesheet">
<style>
  :root {
    --stage: #1c1c1d;
    --card-dark: #2f2f31;
    --card-dark-shade: #3a3a3d;
    --card-light: #ffffff;
    --ink: #2b2b2b;
    --ink-soft: #444444;
    --red: #e1121b;
    --band: #3c3c3e;
    --map: #eeeeee;
    --white: #ffffff;
  }
  * { margin: 0; padding: 0; box-sizing: border-box; }
  html, body { width: 1200px; height: 912px; overflow: hidden; }
  body {
    background: var(--stage);
    font-family: "Open Sans", Arial, sans-serif;
    position: relative;
  }
  .card {
    position: absolute;
    left: 270px;
    width: 660px;
    height: 400px;
    overflow: hidden;
    box-shadow: 0 12px 30px rgba(0,0,0,.45);
  }
  /* front */
  .card-front {
    top: 36px;
    background: radial-gradient(ellipse at 35% 40%, var(--card-dark-shade) 0%, var(--card-dark) 60%);
  }
  .brand {
    display: flex;
    align-items: center;
    gap: 14px;
  }
  .brand-dot {
    width: 44px; height: 44px;
    border-radius: 50%;
    background: var(--red);
    flex: none;
  }
  .brand-name {
    font-weight: 800;
    letter-spacing: -1px;
    line-height: 1;
  }
  .card-front .brand { position: absolute; left: 150px; top: 120px; }
  .card-front .brand-name { color: var(--white); font-size: 64px; }
  .card-front .brand-rule {
    position: absolute; left: 150px; top: 206px;
    width: 390px; height: 4px; background: var(--red);
  }
  .hours {
    position: absolute; left: 0; right: 0; top: 262px;
    text-align: center;
    color: var(--white);
    font-size: 19px;
    line-height: 1.6;
  }
  /* back */
  .card-back { top: 476px; background: var(--card-light); }
  .card-back .brand { position: absolute; left: 36px; top: 30px; }
  .card-back .brand-dot { width: 34px; height: 34px; }
  .card-back .brand-name { color: var(--ink); font-size: 46px; }
  .card-back .brand-rule {
    position: absolute; left: 36px; top: 92px;
    width: 300px; height: 3px; background: var(--red);
  }
  .address {
    position: absolute; left: 84px; top: 110px;
    color: var(--ink-soft); font-size: 15px; line-height: 1.35;
  }
  .division { position: absolute; left: 84px; }
  .division-1 { top: 182px; }
  .division-2 { top: 282px; }
  .division h2 {
    font-size: 16px; font-weight: 800; color: var(--ink); margin-bottom: 2px;
  }
  .contact-list { list-style: none; }
  .contact-list li {
    display: flex; align-items: center; gap: 8px;
    font-size: 13.5px; color: var(--ink-soft); line-height: 1.55;
  }
  .contact-list svg { width: 14px; height: 14px; flex: none; }
  .map {
    position: absolute; right: 24px; top: 24px;
    width: 250px; height: 150px;
    background: var(--map);
    border: 1px solid #d8d8d8;
  }
  .swoosh { position: absolute; inset: 0; pointer-events: none; }
</style>
</head>
<body>

<section class="card card-front" aria-label="Vorderseite">
  <div class="brand">
    <span class="brand-dot"></span>
    <span class="brand-name">Brunnhofer</span>
  </div>
  <div class="brand-rule"></div>
  <div class="hours">
    <p>ÖFFNUNGSZEITEN:</p>
    <p>Mo - Fr / 08.00 - 12.00 Uhr und 13.00 - 17.00 Uhr</p>
  </div>
</section>

<section class="card card-back" aria-label="Rückseite">
  <svg class="swoosh" viewBox="0 0 660 400" preserveAspectRatio="none">
    <path d="M660 210 C560 330 400 392 250 400 L660 400 Z" fill="var(--band)"/>
    <path d="M660 150 C560 300 420 380 240 400 L262 400 C430 378 570 310 660 196 Z" fill="var(--red)"/>
  </svg>

  <div class="brand">
    <span class="brand-dot"></span>
    <span class="brand-name">Brunnhofer</span>
  </div>
  <div class="brand-rule"></div>

  <div class="map" role="img" aria-label="Lageplan mit Straßen rund um den Standort"></div>

  <address class="address">
    Brunnhofer GmbH<br>
    Lindenauer Str. 31<br>
    80993 München
  </address>

  <div class="division division-1">
    <h2>Autoverwertung Autoteile</h2>
    <ul class="contact-list">
      <li><svg viewBox="0 0 16 16"><circle cx="8" cy="8" r="8" fill="var(--red)"/><path d="M5 4.5l1.6-.4.9 2-1 .8a6 6 0 0 0 2.6 2.6l.8-1 2 .9-.4 1.6C8 11.5 4.5 8 5 4.5z" fill="#fff"/></svg>089 - 12 34 56 78</li>
      <li><svg viewBox="0 0 16 16"><circle cx="8" cy="8" r="8" fill="var(--red)"/><rect x="4" y="5" width="8" height="6" fill="#fff"/><path d="M4 5l4 3.2L12 5" stroke="var(--red)" fill="none"/></svg>info@autoverwertung-brunnhofer-beispiel.de</li>
      <li><svg viewBox="0 0 16 16"><circle cx="8" cy="8" r="8" fill="var(--red)"/><circle cx="8" cy="8" r="4" fill="none" stroke="#fff"/><path d="M4 8h8M8 4v8" stroke="#fff"/></svg>www.autoverwertung-brunnhofer-beispiel.de</li>
    </ul>
  </div>

  <div class="division division-2">
    <h2>Autowerkstatt</h2>
    <ul class="contact-list">
      <li><svg viewBox="0 0 16 16"><circle cx="8" cy="8" r="8" fill="var(--red)"/><path d="M5 4.5l1.6-.4.9 2-1 .8a6 6 0 0 0 2.6 2.6l.8-1 2 .9-.4 1.6C8 11.5 4.5 8 5 4.5z" fill="#fff"/></svg>0151 - 00 11 22 3</li>
      <li><svg viewBox="0 0 16 16"><circle cx="8" cy="8" r="8" fill="var(--red)"/><rect x="4" y="5" width="8" height="6" fill="#fff"/><path d="M4 5l4 3.2L12 5" stroke="var(--red)" fill="none"/></svg>info@auto-brunnhofer-beispiel.de</li>
      <li><svg viewBox="0 0 16 16"><circle cx="8" cy="8" r="8" fill="var(--red)"/><circle cx="8" cy="8" r="4" fill="none" stroke="#fff"/><path d="M4 8h8M8 4v8" stroke="#fff"/></svg>www.auto-brunnhofer-beispiel.de</li>
    </ul>
  </div>
</section>

</body>
</html>
```